Real Estate Managemene Company Needs Business Card Design

We have a logo design and just need business cards made now for our business. Please use PDF logo # 3.

Card with Information to be attached shortly.

The card is used for a real estate management company. We will need to add four other employees and their cards.

Industry/Entity Type

Real Estate

Contact Information for Business Card

Tariq Nawabi
President
3187 Thornfield Avenue
Suite 4
Ashford Ridge, IN 60847
Phone 630.471.2286
Fax 630.493.7720
Cell 630.517.8043
pvgrop@mailnest.net

Once design is approved we will have four other employees
Omar Nawabi
Operations Manager

Samira Nawabi
Administrative Manager

Faz Nawabi
Principal

We would need to take out the cell # 630.517.8043 out for the remaining three cards.

Requirements
Must have
• Please use logo attached

```html
<!DOCTYPE html>
<html lang="en">
<head>
<meta charset="utf-8">
<title>Meridian Property Management Group – Business Card</title>
<link href="https://fonts.googleapis.com/css2?family=Alegreya+SC:wght@500&family=Alegreya+Sans:ital,wght@0,400;1,400&display=swap" rel="stylesheet">
<style>
  :root {
    --backdrop: #4a3f3a;
    --card: #151618;
    --card-edge: #222428;
    --gloss: #2c2e32;
    --accent-blue: #3d8fd6;
    --silver: #c9ccd0;
    --text: #e6e7e9;
    --muted: #a9adb3;
  }
  * { margin: 0; padding: 0; box-sizing: border-box; }
  html, body {
    width: 1200px; height: 716px; overflow: hidden;
    background: var(--backdrop);
  }
  .canvas {
    position: relative; width: 1200px; height: 716px;
    background: var(--backdrop);
  }
  .card {
    position: absolute; top: 215px;
    width: 500px; height: 286px;
    background: var(--card);
    border: 1px solid var(--card-edge);
    box-shadow: 0 6px 18px rgba(0,0,0,.35);
    overflow: hidden;
  }
  .card--front { left: 70px; }
  .card--back { left: 630px; }

  /* Front: gloss company name on black */
  .front-mark {
    position: absolute; inset: 0;
    display: flex; align-items: center; justify-content: center; gap: 14px;
  }
  .front-mark__square { width: 26px; height: 26px; background: var(--gloss); }
  .front-mark__name {
    font-family: 'Alegreya Sans', sans-serif; font-weight: 400;
    font-size: 22px; letter-spacing: 1.5px; color: var(--gloss);
    text-transform: uppercase; line-height: 1.2;
  }

  /* Back */
  .frame-lines { position: absolute; left: 0; top: 0; }
  .contact {
    position: absolute; right: 162px; top: 76px;
    text-align: right;
    font-family: 'Alegreya Sans', sans-serif; color: var(--text);
    font-size: 13px; line-height: 1.4;
  }
  .contact__name {
    font-family: 'Alegreya SC', serif; font-weight: 500;
    font-size: 19px; color: var(--accent-blue); letter-spacing: .5px;
    line-height: 1.1;
  }
  .contact__title {
    font-style: italic; font-size: 12px; color: var(--muted);
    margin-bottom: 8px;
  }
  .contact__line { display: flex; justify-content: flex-end; align-items: center; gap: 5px; }
  .icon { width: 10px; height: 10px; fill: var(--muted); }
  .gap { width: 8px; }

  .company {
    position: absolute; right: 24px; top: 90px; width: 124px;
    display: flex; flex-direction: column; align-items: flex-start; gap: 10px;
  }
  .company__square { width: 18px; height: 18px; background: var(--text); }
  .company__name {
    font-family: 'Alegreya Sans', sans-serif; font-weight: 400;
    font-size: 15px; line-height: 1.25; color: var(--text);
    text-transform: uppercase; letter-spacing: 1px;
  }
</style>
</head>
<body>
<main class="canvas">

  <section class="card card--front" aria-label="Card front">
    <div class="front-mark">
      <span class="front-mark__square"></span>
      <span class="front-mark__name">Meridian<br>Property<br>Management</span>
    </div>
  </section>

  <section class="card card--back" aria-label="Card back">
    <svg class="frame-lines" width="500" height="286" viewBox="0 0 500 286" aria-hidden="true">
      <polyline points="140,14 52,20 14,140" fill="none" stroke="var(--accent-blue)" stroke-width="2"/>
      <polyline points="150,26 62,32 24,150" fill="none" stroke="var(--silver)" stroke-width="2.5"/>
      <polyline points="24,150 56,262 150,264" fill="none" stroke="var(--silver)" stroke-width="2.5"/>
      <polyline points="14,150 44,274 120,276" fill="none" stroke="var(--accent-blue)" stroke-width="2"/>
    </svg>

    <div class="contact">
      <div class="contact__name">Tariq Nawabi</div>
      <div class="contact__title">President</div>
      <div class="contact__line">630.517.8043
        <svg class="icon" viewBox="0 0 10 10"><rect x="2.5" y="0" width="5" height="10" rx="1"/></svg>
      </div>
      <div class="contact__line">pvgrop@mailnest.net
        <svg class="icon" viewBox="0 0 10 10"><path d="M0 2h10v6H0z"/></svg>
      </div>
      <div class="contact__line">630.471.2286
        <svg class="icon" viewBox="0 0 10 10"><path d="M1 1c0 5 3 8 8 8l1-2-2-1-1 1C5 6 4 5 3 3l1-1-1-2z"/></svg>
        <span class="gap"></span>630.493.7720
        <svg class="icon" viewBox="0 0 10 10"><rect x="0" y="3" width="10" height="6" rx="1"/><rect x="2" y="0" width="6" height="3"/></svg>
      </div>
      <div class="contact__line">3187 Thornfield Avenue Suite 4</div>
      <div class="contact__line">Ashford Ridge, IN 60847</div>
    </div>

    <div class="company">
      <span class="company__square"></span>
      <span class="company__name">Meridian Property Management Group</span>
    </div>
  </section>

</main>
</body>
</html>
```